Rapidly growing regional logistics company looking for a modern clean website design.

We need a website for a 5 year old company based in New England.
We offer a complete logistics solution. With services dedicated to the changing economic environment. Services to our customers include, same day delivery, trucking and van service, warehouse & storage, pool distribution, and B2B installations.
We've implemented leading technology along the way, that provides visibility, accountability, up to the minute tracking, and project management.
Our goal to be known in the industry we service as an excellent provider of time-critical services and dependability.
Independently of the services we offer, our customers know that they can count on a true partner.

Target Market(s)

B2B, including printers, retail, manufacturers, wholesalers, electronics, any company that needs product delivered or warehoused

Industry/Entity Type

Logistics

Coding

Coded - Design and coding required

Number of Pages Required

5+ page

Font styles to use
Sans Serif

Colors
0255a3

Requirements
Must have
• Clean, modern design, limited clutter. Limited tabs, preferred everything on 1st screen roll down to see info

```html
<!DOCTYPE html>
<html lang="en">
<head>
<meta charset="utf-8">
<title>Ridgeway Logistics</title>
<link rel="stylesheet" href="https://fonts.googleapis.com/css2?family=Lato:wght@400;700;900&family=Open+Sans:wght@400;600;700&display=swap">
<style>
:root{
  --navy:#262f4a;
  --blue:#4169b3;
  --blue-dark:#33589c;
  --ink:#222;
  --text:#444;
  --grey-bg:#ececec;
  --field:#dcdcdc;
  --footer:#4a4a4a;
  --footer-dark:#333;
  --white:#fff;
}
*{box-sizing:border-box;margin:0;padding:0}
html,body{width:1200px;height:3742px;overflow:hidden}
body{font-family:"Open Sans",Arial,sans-serif;color:var(--text);background:var(--white);position:relative}
section,header,footer,nav{position:absolute;left:0;width:1200px}
.abs{position:absolute}
.btn-outline{position:absolute;border:2px solid currentColor;font:400 15px "Open Sans",sans-serif;display:flex;align-items:center;justify-content:center}
h2{font-family:"Lato",sans-serif;font-weight:700;color:var(--ink)}

/* top bar */
.topbar{top:0;height:25px;background:var(--navy);color:var(--white);font-size:12px;font-weight:600}
.topbar .mail{left:120px;top:4px;display:flex;gap:8px;align-items:center}
.social{display:flex;gap:7px}
.topbar .social{position:absolute;right:120px;top:4px}
.social span{width:17px;height:17px;border-radius:50%;background:var(--white);display:block}

/* header */
.site-header{top:25px;height:147px;background:var(--white)}
.brand{left:120px;top:40px;display:flex;align-items:center;gap:12px}
.brand-mark{width:46px;height:46px;border-radius:50%;background:var(--blue)}
.brand-name{font:700 26px/1.05 "Lato",sans-serif;color:var(--navy);letter-spacing:1px}
.contact-item{top:55px;display:flex;gap:10px;align-items:center;font-size:13px;color:var(--ink)}
.contact-item b{font-size:15px;font-weight:600;display:block}
.contact-item small{font-size:12px;color:#777}
.quote-btn{left:940px;top:57px;width:140px;height:40px;background:var(--blue);color:var(--white);font:700 14px "Open Sans",sans-serif;display:flex;align-items:center;justify-content:center;letter-spacing:.5px}

/* nav */
.main-nav{top:172px;height:48px;background:var(--blue);color:var(--white)}
.main-nav a{position:absolute;top:14px;font:700 15px "Open Sans",sans-serif;color:var(--white);text-decoration:none}
.main-nav .sep{position:absolute;top:0;width:1px;height:48px;background:rgba(255,255,255,.25)}
.search{left:873px;top:12px;width:207px;height:24px;background:var(--white);display:flex;justify-content:flex-end;align-items:center;padding-right:6px}

/* hero */
.hero{top:220px;height:548px;background:linear-gradient(180deg,#8fb2d8 0%,#b9cde2 45%,#9aa7b4 75%,#6e7681 100%)}
.hero-overlay{position:absolute;inset:0;background:linear-gradient(90deg,rgba(35,70,140,.85) 0%,rgba(55,95,165,.55) 40%,rgba(80,120,180,0) 70%)}
.hero-title{left:120px;top:195px;font:700 40px/1.15 "Lato",sans-serif;color:var(--white);letter-spacing:2px}
.hero-text{left:120px;top:290px;width:380px;font-size:15px;font-weight:600;color:var(--white)}
.hero .btn-outline{left:120px;top:352px;width:160px;height:44px;color:var(--white)}
.arrow{width:50px;height:50px;border-radius:50%;background:rgba(255,255,255,.85);top:223px;display:flex;align-items:center;justify-content:center}
.dots{top:785px;left:548px;display:flex;gap:12px}
.dots span{width:16px;height:16px;border-radius:50%;background:#333;display:block}
.dots span:first-child{background:var(--blue)}

/* warehousing */
.warehousing{top:768px;height:307px;text-align:center}
.warehousing h2{position:absolute;top:62px;width:100%;font-size:36px;letter-spacing:1px}
.rule{position:absolute;height:4px;background:var(--navy)}
.warehousing p{position:absolute;top:148px;left:120px;width:960px;font-size:15px;line-height:1.6}
.warehousing .btn-outline{left:522px;top:217px;width:156px;height:42px;color:var(--ink)}

/* truck */
.truck{top:1075px;height:572px;background:var(--grey-bg)}
.truck h2{position:absolute;left:120px;top:62px;font-size:35px;letter-spacing:1px}
.truck .lead{left:120px;top:142px;font-size:16px;color:var(--ink)}
.checklist{position:absolute;left:120px;top:190px;width:420px;list-style:none}
.checklist li{display:flex;gap:14px;font-size:14px;color:var(--ink);line-height:1.35;margin-bottom:12px}
.checklist svg{flex:0 0 auto;margin-top:2px}
.truck .btn-outline{left:120px;top:452px;width:157px;height:42px;color:var(--blue)}
.video-frame{left:606px;top:104px;width:474px;height:372px;background:#cfcfcf;padding:10px}
.video-frame div{width:100%;height:100%;background:linear-gradient(180deg,#e4e9ee 0%,#b9c3cc 55%,#6d757c 100%);position:relative}
.play{position:absolute;left:50%;top:50%;transform:translate(-50%,-50%)}

/* distribution */
.distribution{top:1647px;height:566px}
.pool-photo{left:0;top:0;width:600px;height:566px;background:linear-gradient(180deg,#2f7ed3 0%,#8ec3ec 38%,#4fb0d8 60%,#1d8fc4 100%)}
.dist-panel{left:600px;top:0;width:600px;height:566px;background:var(--blue);color:var(--white)}
.dist-panel h3{position:absolute;left:59px;top:64px;font:700 31px "Lato",sans-serif}
.dist-panel .rule{left:59px;top:108px;width:90px;background:var(--white)}
.dist-panel .copy{position:absolute;left:59px;top:128px;width:452px;font-size:14px;font-weight:600;line-height:1.6}
.dist-panel .copy p{margin-bottom:22px}
.dist-panel .btn-outline{left:59px;top:441px;width:157px;height:42px;color:var(--white)}

/* features */
.features{top:2213px;height:524px}
.feature{position:absolute;top:0;width:297px}
.feature h3{position:absolute;top:92px;font:700 22px "Lato",sans-serif;color:var(--ink);white-space:nowrap}
.feature .rule{top:128px;width:90px}
.feature .photo{position:absolute;top:168px;width:297px;height:170px}
.feature p{position:absolute;top:370px;font-size:14px;line-height:1.55;color:var(--ink)}
.feature .meta{position:absolute;top:355px;font-size:12px;color:var(--ink)}
.read-more{position:absolute;top:490px;font:700 10px "Open Sans",sans-serif;color:var(--blue);letter-spacing:.3px}

/* quote */
.quote{top:2737px;height:507px;background:var(--grey-bg)}
.quote h2{position:absolute;left:120px;top:86px;font-size:26px}
.quote .rule{left:120px;top:122px;width:90px}
.quote .intro{left:120px;top:140px;font-size:13px;font-weight:600;color:var(--ink)}
.field{position:absolute;height:37px;background:var(--field);font-size:13px;color:#888;display:flex;align-items:center;justify-content:space-between;padding:0 14px}
.submit{left:120px;top:387px;width:638px;height:37px;background:var(--blue);color:var(--white);font:600 14px "Open Sans",sans-serif;display:flex;align-items:center;justify-content:center}
.promo{left:786px;top:58px;width:294px;height:364px}
.promo .photo{width:294px;height:294px;background:linear-gradient(180deg,#dfe6ec 0%,#c7d3de 60%,#9cafc2 100%)}
.promo .caption{height:70px;background:#2d7fc6;color:var(--white);padding:12px 14px}
.promo .caption b{font:700 18px "Lato",sans-serif;display:block}
.promo .caption small{font-size:11px}

/* newsletter */
.newsletter{top:3244px;height:219px;background:var(--blue);color:var(--white);text-align:center}
.newsletter h2{color:var(--white);position:absolute;top:48px;width:100%;font-size:26px;font-weight:900;letter-spacing:1.5px}
.newsletter .sub{position:absolute;top:83px;width:100%;font:700 15px "Lato",sans-serif;letter-spacing:1.5px}
.sub-form{left:342px;top:119px;width:561px;height:60px;background:var(--white);padding:12px 25px}
.sub-form .input{position:absolute;left:25px;top:16px;width:411px;height:28px;border:1px solid #ccc;font-size:10px;color:#777;text-align:left;padding:7px 8px}
.sub-form .go{position:absolute;left:436px;top:16px;width:100px;height:28px;background:var(--blue);font:700 14px "Open Sans",sans-serif;display:flex;align-items:center;justify-content:center}

/* footer */
.site-footer{top:3463px;height:222px;background:var(--footer);color:var(--white)}
.site-footer h4{font:700 15px "Open Sans",sans-serif;position:absolute}
.footer-rule{position:absolute;height:2px;width:55px;background:var(--white)}
.about p{font-size:13px;font-weight:600;line-height:1.35}
.links{list-style:none;font-size:13px;font-weight:600}
.links li{display:flex;gap:14px;align-items:center;height:22px}
.office{list-style:none;font-size:13px;font-weight:600}
.office li{display:flex;gap:14px;align-items:center;height:22px}
.bottom-bar{top:3685px;height:57px;background:var(--footer-dark);color:#ccc}
.bottom-bar p{position:absolute;left:120px;top:19px;font-size:13px}
.bottom-bar .social{position:absolute;right:120px;top:14px;gap:12px}
.bottom-bar .social span{width:28px;height:28px;border:2px solid #ccc;background:transparent}
</style>
</head>
<body>

<div class="topbar">
  <div class="abs mail">
    <svg width="14" height="10" viewBox="0 0 14 10"><rect x=".5" y=".5" width="13" height="9" fill="none" stroke="#fff"/><path d="M.5 .5 7 6 13.5 .5" fill="none" stroke="#fff"/></svg>
    info@ridgewayfreight.net
  </div>
  <div class="social"><span></span><span></span><span></span><span></span><span></span></div>
</div>

<header class="site-header">
  <div class="abs brand">
    <span class="brand-mark"></span>
    <span class="brand-name">RIDGEWAY<br>LOGISTICS</span>
  </div>
  <div class="abs contact-item" style="left:505px">
    <svg width="34" height="34" viewBox="0 0 34 34"><circle cx="17" cy="17" r="15.5" fill="none" stroke="#4169b3" stroke-width="2"/><path d="M12 10c1-1 2-1 3 0l1.5 2.5c.5 1 0 1.7-.8 2.3 .8 1.8 2.2 3.2 4 4 .6-.8 1.3-1.3 2.3-.8L24.5 20c1 1 1 2 0 3-2 2-6 1-9.5-2.5S10 12 12 10z" fill="#4169b3"/></svg>
    <div><b>+0 555 010 2040</b><small>info@ridgeway.net</small></div>
  </div>
  <div class="abs contact-item" style="left:688px">
    <svg width="34" height="34" viewBox="0 0 34 34"><circle cx="17" cy="17" r="15.5" fill="none" stroke="#4169b3" stroke-width="2"/><path d="M17 9v8l5 4" fill="none" stroke="#4169b3" stroke-width="2.2"/></svg>
    <div><b>Mon-Sat: 9:00AM-6:00PM</b><small>Opening Time</small></div>
  </div>
  <div class="abs quote-btn">GET A QUOTE</div>
</header>

<nav class="main-nav">
  <span class="sep" style="left:100px"></span>
  <a style="left:125px">Home</a><span class="sep" style="left:200px"></span>
  <a style="left:225px">Features</a><span class="sep" style="left:325px"></span>
  <a style="left:350px">Services <small>&#9662;</small></a><span class="sep" style="left:450px"></span>
  <a style="left:474px">About Us</a><span class="sep" style="left:580px"></span>
  <a style="left:606px">News</a><span class="sep" style="left:680px"></span>
  <a style="left:706px">Contact Us</a><span class="sep" style="left:830px"></span>
  <div class="abs search">
    <svg width="12" height="12" viewBox="0 0 12 12"><circle cx="5" cy="5" r="3.8" fill="none" stroke="#333" stroke-width="1.6"/><path d="M8 8l3 3" stroke="#333" stroke-width="1.6"/></svg>
  </div>
</nav>

<section class="hero" role="img" aria-label="Cargo pallet being loaded onto a freight aircraft by a scissor lift">
  <div class="hero-overlay"></div>
  <div class="abs hero-title">WE FRIGHT TO ALL<br>OVER THER WORLD</div>
  <p class="abs hero-text">Lorem Ipsum is simply dummy text of the printing and typesetting industry.</p>
  <div class="btn-outline">Read More</div>
  <div class="abs arrow" style="left:55px"><svg width="20" height="20" viewBox="0 0 20 20"><path d="M13 3 6 10l7 7z" fill="#333"/></svg></div>
  <div class="abs arrow" style="right:55px"><svg width="20" height="20" viewBox="0 0 20 20"><path d="M7 3l7 7-7 7z" fill="#333"/></svg></div>
</section>

<div class="abs dots"><span></span><span></span><span></span><span></span></div>

<section class="warehousing">
  <h2>Warehousing</h2>
  <span class="rule" style="left:555px;top:116px;width:90px"></span>
  <p>Our warehouse facility may prove to be one of the most valuable extensions of your company's operations. With a secure warehouse conveniently located in central New England to&nbsp; supplement your firm's storage and distribution needs.</p>
  <div class="btn-outline">Read More</div>
</section>

<section class="truck">
  <h2>Truck &amp; Van Service</h2>
  <span class="rule" style="left:120px;top:110px;width:90px"></span>
  <p class="abs lead">Trucking, vehicle and ground transportation include:</p>
  <ul class="checklist">
    <li><svg width="14" height="14" viewBox="0 0 14 14"><circle cx="7" cy="7" r="6" fill="none" stroke="#4169b3" stroke-width="1.5"/><path d="M4 7l2 2 4-4" fill="none" stroke="#4169b3" stroke-width="1.5"/></svg>Rush and pre-scheduled delivery</li>
    <li><svg width="14" height="14" viewBox="0 0 14 14"><circle cx="7" cy="7" r="6" fill="none" stroke="#4169b3" stroke-width="1.5"/><path d="M4 7l2 2 4-4" fill="none" stroke="#4169b3" stroke-width="1.5"/></svg>Light and heavy trucking (cargo vans to liftgates)</li>
    <li><svg width="14" height="14" viewBox="0 0 14 14"><circle cx="7" cy="7" r="6" fill="none" stroke="#4169b3" stroke-width="1.5"/><path d="M4 7l2 2 4-4" fill="none" stroke="#4169b3" stroke-width="1.5"/></svg>Line haul from pick up locations to airports and other designated locations</li>
    <li><svg width="14" height="14" viewBox="0 0 14 14"><circle cx="7" cy="7" r="6" fill="none" stroke="#4169b3" stroke-width="1.5"/><path d="M4 7l2 2 4-4" fill="none" stroke="#4169b3" stroke-width="1.5"/></svg>Expedited ground services</li>
    <li><svg width="14" height="14" viewBox="0 0 14 14"><circle cx="7" cy="7" r="6" fill="none" stroke="#4169b3" stroke-width="1.5"/><path d="M4 7l2 2 4-4" fill="none" stroke="#4169b3" stroke-width="1.5"/></svg>LTL (Less than Truckload)</li>
    <li><svg width="14" height="14" viewBox="0 0 14 14"><circle cx="7" cy="7" r="6" fill="none" stroke="#4169b3" stroke-width="1.5"/><path d="M4 7l2 2 4-4" fill="none" stroke="#4169b3" stroke-width="1.5"/></svg>Late-night delivery — we are open 24 hours per day, 365 days per year</li>
    <li><svg width="14" height="14" viewBox="0 0 14 14"><circle cx="7" cy="7" r="6" fill="none" stroke="#4169b3" stroke-width="1.5"/><path d="M4 7l2 2 4-4" fill="none" stroke="#4169b3" stroke-width="1.5"/></svg>Truckload</li>
  </ul>
  <div class="btn-outline">Read More</div>
  <div class="abs video-frame">
    <div role="img" aria-label="White cargo van parked on a street">
      <svg class="play" width="48" height="48" viewBox="0 0 48 48"><circle cx="24" cy="24" r="22" fill="rgba(0,0,0,.25)" stroke="#fff" stroke-width="2.5"/><path d="M19 14l14 10-14 10z" fill="#fff"/></svg>
    </div>
  </div>
</section>

<section class="distribution">
  <div class="abs pool-photo" role="img" aria-label="Swimming pool ladder with blue sea and sky behind"></div>
  <div class="abs dist-panel">
    <h3>Distribution &amp; Pool Services</h3>
    <span class="rule"></span>
    <div class="copy">
      <p>Pool Distribution is the distribution of product to numerous customers within a particular geographic region.</p>
      <p>This is a highly superior and cost-effective alternative to the higher cost of LTL shipments. In some instances, this could represent a 30%-70% savings vs. traditional LTL. Instead of LTL direct to customer, product is shipped to the Ridgeway regional warehouse in truckload quantities.</p>
      <p>There it is off loaded, then segregated and sorted by customer and then reloaded on local delivery trucks.</p>
    </div>
    <div class="btn-outline">Read More</div>
  </div>
</section>

<section class="features">
  <div class="feature" style="left:120px">
    <h3>Same-day Delivery Service</h3><span class="rule"></span>
    <div class="photo" role="img" aria-label="Courier handing a parcel to a customer" style="background:linear-gradient(135deg,#e8e6e0 0%,#c9b28e 50%,#6fae57 100%)"></div>
    <p>Regardless of the specifics of your needs, RIDGEWAY can handle your same-day delivery needs. Ridgeway Logistics offers same-day delivery services as a standalone service or insupport of our other services.</p>
    <span class="read-more">READ MORE &nbsp;&rarr;</span>
  </div>
  <div class="feature" style="left:454px">
    <h3>Dedicated Delivery Service</h3><span class="rule"></span>
    <div class="photo" role="img" aria-label="Worker in a warehouse holding a phone" style="background:linear-gradient(135deg,#c7d3e2 0%,#8fb0d6 45%,#c79a6a 100%)"></div>
    <p>Our goal is to make the process easy, and of course, to make you look good in the eyes of your customers and suppliers. Whether your needs are a car to tractor trailer Ridgeway can provide the solution for you.</p>
    <span class="read-more">READ MORE &nbsp;&rarr;</span>
  </div>
  <div class="feature" style="left:786px">
    <h3>Latest News</h3><span class="rule"></span>
    <div class="photo" role="img" aria-label="Row of white trucks parked side by side" style="background:linear-gradient(180deg,#dfe9f3 0%,#f2f4f6 50%,#8d969e 100%)"></div>
    <span class="meta">By Admin &nbsp;/ 30th Sep, 2015 &nbsp;/ Shipping</span>
    <p style="top:378px">Lorem Ipsum is simply dummy text of the printing and typesetting industry.Lorem&nbsp; Ipsum is simply dummy text of the printing and type setting industry.</p>
    <span class="read-more">READ MORE &nbsp;&rarr;</span>
  </div>
</section>

<section class="quote">
  <h2>Get a Quote</h2>
  <span class="rule"></span>
  <p class="abs intro">Lorem Ipsum is simply dummy text of the print ing and typesetting industry.</p>
  <div class="field" style="left:120px;top:197px;width:307px">Sender Name</div>
  <div class="field" style="left:454px;top:197px;width:304px">Cargo Type <small>&#9662;</small></div>
  <div class="field" style="left:120px;top:257px;width:307px">Destination</div>
  <div class="field" style="left:454px;top:257px;width:304px">Transport Type <small>&#9662;</small></div>
  <div class="field" style="left:120px;top:322px;width:638px">Message</div>
  <div class="abs submit">SUBMIT</div>
  <div class="abs promo">
    <div class="photo" role="img" aria-label="Delivery worker holding a parcel and a clipboard"></div>
    <div class="caption"><b>On Every Transportation</b><small>More Than 2000 Km's</small></div>
  </div>
</section>

<section class="newsletter">
  <h2>SUBSCRIBE TO OUR NEWSLETTER</h2>
  <p class="sub">TO RECEIVE THE LATEST NEWS &amp; UPDATE</p>
  <div class="abs sub-form">
    <div class="input">Your E-mail</div>
    <div class="go">SUBMIT</div>
  </div>
</section>

<footer class="site-footer">
  <h4 style="left:120px;top:38px">ABOUT US</h4>
  <span class="footer-rule" style="left:120px;top:60px"></span>
  <div class="abs about" style="left:120px;top:75px;width:300px">
    <p>Our company was founded in 2012 but our team is seasoned, with a combined 75 years of experience.</p>
    <p style="margin-top:18px">Ridgeway Logistics offers a complete logistics solution. With services dedicated.</p>
    <p style="margin-top:14px;font-weight:700">READ MORE.....</p>
  </div>
  <h4 style="left:599px;top:38px">QUICK LINKS</h4>
  <span class="footer-rule" style="left:599px;top:60px"></span>
  <ul class="abs links" style="left:599px;top:74px">
    <li>&rsaquo;<span>Home</span></li><li>&rsaquo;<span>Features</span></li><li>&rsaquo;<span>Services</span></li><li>&rsaquo;<span>News</span></li><li>&rsaquo;<span>Contact</span></li>
  </ul>
  <h4 style="left:918px;top:38px">TRANSPORT OFFICE</h4>
  <span class="footer-rule" style="left:918px;top:60px"></span>
  <ul class="abs office" style="left:886px;top:74px">
    <li><svg width="12" height="14" viewBox="0 0 12 14"><path d="M6 13S1 8 1 5a5 5 0 0110 0c0 3-5 8-5 8z" fill="#fff"/></svg>1234, Your, Full Address.</li>
    <li><svg width="12" height="12" viewBox="0 0 12 12"><path d="M2 1c1-1 2 0 2.5 1l.7 1.5c.3.7-.2 1.2-.7 1.6.6 1.3 1.5 2.2 2.8 2.8.4-.5.9-1 1.6-.7L10.4 8c1 .5 1.5 1.5.5 2.5C9 12 5 10 3.5 8.5S0 3 2 1z" fill="#fff"/></svg>+0 555 010 2040</li>
    <li><svg width="12" height="10" viewBox="0 0 12 10"><rect x=".5" y=".5" width="11" height="9" fill="none" stroke="#fff"/><path d="M.5.5 6 5.5 11.5.5" fill="none" stroke="#fff"/></svg>info@ridgewaylogistic.net</li>
    <li><svg width="12" height="12" viewBox="0 0 12 12"><rect x="1" y="4" width="10" height="6" fill="#fff"/><rect x="3" y="1" width="6" height="3" fill="none" stroke="#fff"/></svg>+0 555 010 2040</li>
    <li><svg width="12" height="12" viewBox="0 0 12 12"><circle cx="6" cy="6" r="5" fill="none" stroke="#fff"/><path d="M6 3v3l2 1.5" fill="none" stroke="#fff"/></svg>Mon-Sat 9:00am-6.00pm</li>
  </ul>
</footer>

<div class="abs bottom-bar" style="left:0;width:1200px">
  <p>© 2017 Ridgeway Logistics - All Rights Reserved</p>
  <div class="social"><span></span><span></span><span></span><span></span><span></span></div>
</div>

</body>
</html>
```